Flyer for Compassion training days

I need a A5-size, single-sided flyer design for my training days. They are weekends in a blend of Compassionate Communication and Buddhist teachings called Palomere Communication. The logo for Palomere that should be included.
The flyer needs room for 1) course title, 2) course dates, location & price, 3) course description, 4) booking info, 5) my picture & short bio, and 6) the palomere.co website (yes, it is 'co' and not 'com).
Updates

Target Market(s)

Women 35-65 years, well-educated, spiritually minded. May have interests like yoga and meditation.

Industry/Entity Type

Health And Wellness

Font styles to use
Sans Serif
Other font styles liked:
• Blue Plaque, Josefina are both great

Colors
fbf289
fdf9cf
cfeae6
33b8a4

Requirements
Must have
• The Palomere logo; my picture.
• Elegance. Calm and expansive feel.
• The poster provided in the project files shows you the kind of information I need to include.
• Colours -- greens and yellows, but the options on pixel harbor are not quite the right shades.
• The logo colour can be changed.
Nice to have
• Classy (but not cliche) image associated with Buddhism; gentle curves similar to those on the business card (see project files).
Should not have
• Dark background. Busy, loud design. Overly 'swirly' design. Images that I have to buy separately.

```html
<!DOCTYPE html>
<html lang="en">
<head>
<meta charset="utf-8">
<title>Palomere Communication – Core Course Flyer</title>
<link href="https://fonts.googleapis.com/css2?family=Josefin+Sans:wght@300;400;600&display=swap" rel="stylesheet">
<style>
  :root {
    --backdrop: #1fae4b;
    --paper-light: #fdfbe8;
    --paper-warm: #f6f1cf;
    --brand-green: #2aae4f;
    --brand-green-light: #7dc36b;
    --ink: #2b2b2b;
    --ink-soft: #3d3d3d;
    --gold-light: #e9c96d;
    --gold-dark: #9a7424;
    --sepia-light: #c9a877;
    --sepia-dark: #5a4226;
    --bubble: rgba(160, 205, 190, 0.25);
  }
  * { box-sizing: border-box; margin: 0; padding: 0; }
  html, body {
    width: 1200px; height: 1200px; overflow: hidden;
    background: var(--backdrop);
    font-family: "Josefin Sans", sans-serif;
    color: var(--ink);
  }
  .flyer {
    position: absolute; left: 230px; top: 78px;
    width: 740px; height: 1044px;
    background: radial-gradient(ellipse at 55% 45%, var(--paper-light) 0%, var(--paper-light) 45%, var(--paper-warm) 100%);
    overflow: hidden;
  }
  .bubble { position: absolute; border-radius: 50%; background: var(--bubble); }

  .brand { position: absolute; left: 448px; top: 46px; display: flex; align-items: center; gap: 14px; }
  .brand-dot { width: 54px; height: 54px; border-radius: 50%; background: var(--brand-green); }
  .brand-name { font-size: 27px; font-weight: 400; color: var(--brand-green); }

  .figure-art {
    position: absolute; left: 40px; top: 86px; width: 206px; height: 298px;
    border-radius: 46% 46% 30% 30%;
    background: radial-gradient(ellipse at 50% 40%, var(--gold-light), var(--gold-dark));
  }
  .flourish-art {
    position: absolute; left: 420px; top: 120px; width: 320px; height: 380px;
    background: radial-gradient(ellipse at 50% 40%, rgba(200, 215, 150, 0.35), rgba(253, 251, 232, 0) 70%);
  }

  .headline {
    position: absolute; left: 258px; top: 208px; width: 456px;
    text-align: center; font-weight: 400; line-height: 1.5;
  }
  .headline .formula { display: block; font-size: 24px; }
  .headline .title { display: block; font-size: 36px; font-weight: 600; line-height: 1.15; white-space: nowrap; }

  .tag {
    position: absolute; height: 36px; background: var(--brand-green);
    color: #fff; font-size: 26px; display: flex; align-items: center; justify-content: center;
    padding-top: 4px; letter-spacing: 0.5px;
  }
  .tag-course { left: 253px; top: 396px; width: 248px;
    clip-path: polygon(0 0, 100% 0, 94% 50%, 100% 100%, 0 100%, 6% 50%); }
  .tag-booking { left: 0; top: 802px; width: 158px; height: 32px; font-size: 22px;
    background: linear-gradient(90deg, var(--brand-green-light), var(--brand-green));
    clip-path: polygon(0 0, 92% 0, 100% 50%, 92% 100%, 0 100%); }

  .event-details {
    position: absolute; left: 130px; top: 440px; width: 500px;
    text-align: center; font-size: 24px; font-weight: 400; line-height: 1.25;
  }

  .description {
    position: absolute; left: 46px; top: 522px; width: 650px;
    font-size: 15px; font-weight: 300; line-height: 1.35; color: var(--ink-soft);
  }
  .description p { margin-bottom: 8px; }
  .description ul { list-style: none; margin: 2px 0 14px 10px; }
  .description li { display: flex; align-items: center; gap: 10px; margin-bottom: 3px; font-size: 14px; }
  .description li svg { flex: none; }

  .booking-line {
    position: absolute; left: 166px; top: 808px; font-size: 20px; font-weight: 400;
  }

  .portrait {
    position: absolute; left: 49px; top: 864px; width: 134px; height: 132px;
    border-radius: 10px; border: 2px solid var(--sepia-dark);
    background: radial-gradient(ellipse at 50% 45%, var(--sepia-light), var(--sepia-dark));
  }
  .bio {
    position: absolute; left: 192px; top: 880px; width: 500px;
    font-size: 14.5px; font-weight: 400; line-height: 1.2;
  }
  .bio p { margin-bottom: 8px; }
</style>
</head>
<body>
  <main class="flyer">
    <span class="bubble" style="left:470px;top:110px;width:60px;height:60px"></span>
    <span class="bubble" style="left:640px;top:380px;width:90px;height:90px"></span>
    <span class="bubble" style="left:600px;top:620px;width:70px;height:70px"></span>
    <span class="bubble" style="left:380px;top:700px;width:50px;height:50px"></span>
    <span class="bubble" style="left:560px;top:960px;width:80px;height:80px"></span>
    <span class="bubble" style="left:110px;top:560px;width:40px;height:40px"></span>

    <div class="flourish-art" role="img" aria-label="Delicate swirling vines with a small butterfly"></div>

    <div class="brand">
      <span class="brand-dot"></span>
      <span class="brand-name">Palomere.co</span>
    </div>

    <div class="figure-art" role="img" aria-label="Golden seated Buddha statue"></div>

    <h1 class="headline">
      <span class="formula">Mindfulness + Kindness +</span>
      <span class="formula">Compassionate Communication =</span>
      <span class="title">Palomere Communication</span>
    </h1>

    <div class="tag tag-course">CORE COURSE</div>

    <p class="event-details">11-12 Dec; Rowan Centre, Edinburgh<br>(£125/100)</p>

    <section class="description">
      <p>Palomere Communication can help you increase awareness &amp; compassion in everyday speech (with yourself &amp; others), better understand your own patterns, and build resilience to challenging situations. Choose from:</p>
      <p>In this 2-day Core Course, we’ll explore:</p>
      <ul>
        <li><svg width="14" height="14" viewBox="0 0 14 14"><path d="M2 12 C2 5 6 2 12 2 C12 8 8 12 2 12Z" fill="var(--brand-green)"/></svg>Compassionate Communication;</li>
        <li><svg width="14" height="14" viewBox="0 0 14 14"><path d="M2 12 C2 5 6 2 12 2 C12 8 8 12 2 12Z" fill="var(--brand-green)"/></svg>Buddhist teachings on Right Speech, loving-kindness, Right Effort, and more;</li>
        <li><svg width="14" height="14" viewBox="0 0 14 14"><path d="M2 12 C2 5 6 2 12 2 C12 8 8 12 2 12Z" fill="var(--brand-green)"/></svg>mindfulness practices;</li>
        <li><svg width="14" height="14" viewBox="0 0 14 14"><path d="M2 12 C2 5 6 2 12 2 C12 8 8 12 2 12Z" fill="var(--brand-green)"/></svg>choices available to us in our everyday speech.</li>
      </ul>
      <p>This workshop will be of interest if you’d like to improve personal and/or professional relationships. Open to all, best suited to those with at least 1 year’s experience with Mindfulness, Buddhism, or Compassionate Communication / NVC.</p>
    </section>

    <div class="tag tag-booking">BOOKING</div>
    <p class="booking-line">Book online at Ticketnest or write marisol@palomere.co</p>

    <div class="portrait" role="img" aria-label="Portrait photo of the facilitator"></div>
    <section class="bio">
      <p>Facilitator: Marisol Avendale is an experienced group facilitator, having worked with a range of organisations and presented at a number of festivals &amp; conferences.</p>
      <p>Marisol offers coaching in Palomere Communication.</p>
      <p>For more info, please visit website www.palomere.co</p>
    </section>
  </main>
</body>
</html>
```